Gutschein-Design für Bauträgerfirma
Sehr guter Designer, würde ich immer wieder weiter empfehlen.
Zielgruppe
Wir sind eine Bauträgerfirma und verkaufen Wohnungen für die gehobene Klasse.
Aufgabenstellung
Auflösung min. 150dpi, Format: 3,56m x 2,52m,
Dieses Banner soll eine Werbung bzw. einen Gutschein enthalten.
Folgender Text soll enthalten sein: Wenn Sie eine Wohnung bis zum 31.12.2018 bei uns kaufen, erhalten Sie einen Bemusterungsgutschein von 5.000€.
Der Text kann natürlich auch anders formuliert werden, der Kern sollte erhalten bleiben.
Die Unterlagen können auch im anderen Format zur Verfügung gestellt werden. Es sind alle Render in großem Format verfügbar.

```html
<!DOCTYPE html>
<html lang="de">
<head>
<meta charset="utf-8">
<title>Varnholt Wohnbau – Bemusterungsgutschein</title>
<link rel="stylesheet" href="https://fonts.googleapis.com/css2?family=Overpass:wght@700&family=Archivo+Black&display=swap">
<style>
  :root {
    --navy: #253a63;
    --red: #e5202a;
    --white: #ffffff;
    --bg-light: #f7f2ef;
    --bg-peach: #ecc8b0;
    --bg-warm: #d9a385;
    --bg-dark: #2b1911;
  }
  html, body {
    margin: 0;
    padding: 0;
    width: 1200px;
    height: 849px;
    overflow: hidden;
    background: var(--bg-light);
  }
  .banner {
    position: relative;
    width: 1200px;
    height: 849px;
    overflow: hidden;
    font-family: "Overpass", "Helvetica Neue", Arial, sans-serif;
  }
  .banner-photo {
    position: absolute;
    inset: 0;
    background:
      linear-gradient(90deg,
        var(--bg-light) 0%,
        #f4e6dc 22%,
        var(--bg-peach) 42%,
        #e9bfa4 62%,
        var(--bg-warm) 80%,
        #c58f70 87%,
        var(--bg-dark) 89%,
        #1e110c 100%);
  }
  .brand-box {
    position: absolute;
    left: 44px;
    top: 14px;
    width: 522px;
    height: 264px;
    background: var(--white);
    display: flex;
    align-items: center;
    justify-content: center;
    gap: 16px;
  }
  .brand-mark {
    width: 22px;
    height: 22px;
    background: var(--navy);
  }
  .brand-name {
    font-weight: 700;
    font-size: 42px;
    color: var(--navy);
    white-space: nowrap;
  }
  .offer-text {
    position: absolute;
    left: 44px;
    top: 338px;
    margin: 0;
    font-weight: 700;
    font-size: 48px;
    line-height: 60px;
    color: var(--navy);
    white-space: nowrap;
  }
  .offer-date {
    display: inline-block;
    margin-left: 28px;
    padding: 6px 15px 0;
    line-height: 60px;
    background: var(--red);
    color: var(--white);
    font-size: 56px;
    letter-spacing: 0.5px;
    vertical-align: -6px;
  }
  .voucher-value {
    position: absolute;
    left: 86px;
    top: 706px;
    width: 422px;
    height: 128px;
    background: var(--red);
    color: var(--white);
    font-family: "Archivo Black", "Arial Black", sans-serif;
    font-size: 124px;
    line-height: 132px;
    text-align: center;
    letter-spacing: -2px;
  }
</style>
</head>
<body>
  <main class="banner">
    <div class="banner-photo" role="img" aria-label="Foto: Schlüssel mit silbernem Hausanhänger steckt im Schloss einer geöffneten Wohnungstür"></div>

    <div class="brand-box">
      <span class="brand-mark"></span>
      <span class="brand-name">Varnholt Wohnbau</span>
    </div>

    <p class="offer-text">
      Wenn Sie eine Wohnung<br>
      bis zum <span class="offer-date">31.12.2018</span><br>
      bei uns kaufen, erhalten<br>
      Sie einen<br>
      Bemusterungsgutschein<br>
      von
    </p>

    <div class="voucher-value">5000€</div>
  </main>
</body>
</html>
```